Banner ad to sell prefabricated holiday homes in New Zealand

Harbourlight Homes build prefabricated homes in a factory that are then transported by truck to their site. It's coming into summer here in New Zealand and many people will be thinking about the holidays and wishing they had a holiday home.

The design should communicate some of the following benefits of our homes:
- Full project management
- Great value for money
- Delivered complete with all interior & exterior fittings
- Quality construction in our controlled factory

The banner ad will be displayed on a popular weather website www.skyreport.co.nz
Size: 760px x 120px
Would like it to be animated if but the size must be below 60kb.

I'll upload some nice holiday destination photos for backgrounds & some pictures of our holiday home designs for you to use.
Our main company colors are bright blue (pantone 3005) and light grey/silver.

Updatefor brief:
I would like the animation to show different text so that it's not all squashed up on the one image.
For example have "Prefabricated Holiday Homes" on one image & then it fades/changes to next image with "Delivered complete with all interior & exterior fittings". Or something like that with nice background images or pictures of our houses.

Font styles to use
Sans Serif

Colors
3176b5
0d5aa6
33a6d7
3276b5

Requirements
Nice to have
• Our logo

```html
<!DOCTYPE html>
<html lang="en">
<head>
<meta charset="utf-8">
<title>Harbourlight Homes – Holiday Homes Banner</title>
<link rel="stylesheet" href="https://fonts.googleapis.com/css2?family=Arimo:wght@400;700&display=swap">
<style>
  :root {
    --page-bg: #ececec;
    --brand-blue: #0d5aa6;
    --brand-blue-mid: #3176b5;
    --photo-tone: #7c8579;
    --logo-panel: #ffffff;
    --logo-ink: #2b2b2b;
    --text-light: #ffffff;
  }

  html, body {
    margin: 0;
    width: 1200px;
    height: 900px;
    overflow: hidden;
    background: var(--page-bg);
  }

  .stage {
    position: relative;
    width: 1200px;
    height: 900px;
  }

  .banner-frame {
    position: absolute;
    left: 30px;
    top: 360px;
    width: 1140px;
    height: 180px;
  }

  .banner {
    position: absolute;
    left: 0;
    top: 0;
    width: 760px;
    height: 120px;
    overflow: hidden;
    transform: scale(1.5);
    transform-origin: 0 0;
    font-family: "Arimo", Arial, sans-serif;
    background: var(--brand-blue);
  }

  .banner-shapes {
    position: absolute;
    inset: 0;
    width: 760px;
    height: 120px;
  }

  .headline {
    position: absolute;
    left: 0;
    top: 14px;
    width: 162px;
    margin: 0;
    text-align: center;
    color: var(--text-light);
    font-size: 18.5px;
    font-weight: 700;
    line-height: 30px;
    white-space: nowrap;
  }

  .benefit {
    position: absolute;
    left: 207px;
    top: 43px;
    margin: 0;
    color: var(--text-light);
    font-size: 13.6px;
    font-weight: 400;
    line-height: 16.5px;
    white-space: nowrap;
  }

  .brand {
    position: absolute;
    left: 251px;
    top: 2px;
    height: 21px;
    display: flex;
    align-items: center;
    gap: 8px;
    color: var(--logo-ink);
    font-size: 13px;
    font-weight: 700;
    white-space: nowrap;
  }

  .brand-square {
    width: 18px;
    height: 18px;
    background: var(--brand-blue-mid);
  }
</style>
</head>
<body>
<main class="stage">
  <div class="banner-frame">
    <section class="banner" aria-label="Harbourlight Homes holiday homes banner">
      <svg class="banner-shapes" viewBox="0 0 760 120" xmlns="http://www.w3.org/2000/svg">
        <rect class="house-photo" x="300" y="0" width="460" height="120" fill="var(--photo-tone)"
              role="img" aria-label="Photo of a single-storey prefabricated holiday home with a timber deck and outdoor furniture"/>
        <polygon class="blue-panel" points="0,0 447,0 323,120 0,120" fill="var(--brand-blue)"/>
        <polygon class="logo-panel" points="235,0 453,0 427,25 235,25" fill="var(--logo-panel)"/>
      </svg>

      <h1 class="headline">Prefabricated<br>Holiday Homes In<br>New Zealand</h1>

      <p class="benefit">Delivered complete with all<br>interior &amp; exterior fittings</p>

      <div class="brand">
        <span class="brand-square"></span>
        <span class="brand-name">Harbourlight Homes</span>
      </div>
    </section>
  </div>
</main>
</body>
</html>
```